Torvin Electrics Flyer Design Advertising

I am after an A5 Flyer design to help promote my electrical services business.
I would like to have information on what my business offers, photos of electrical work, and specials/deals for an amount of time.

Industry/Entity Type

Electrician

Font styles to use
Sans Serif

Colors
0292cd
33a6d7
85cae6
3176b5
333333
1b1b1b
ffffff
5c5c5c
474747

Requirements
Must have
• Specialising in New homes, renovations and commercial projects
• Contact details:
• ph. 0457 613 948
• email admin@torvinelectrics.com.au
• facebook TorvinElectrics
• Specials/Deals:
• 10% off all electrical services
• or
• Free LED downlights on installation
• *Terms conditions apply
• ALL RESIDENTIAL & COMMERCIAL ELECTRICAL SERVICES
• - New Home installations
• - Commercial projects
• - Shop fit outs
• - Renovations
• - Smoke Detectors
• - Air Conditioning and Ceiling Fans
• - Garden Lighting
• - Oven and Cooktop Installations
• - Power Point installation
• - LED lighting upgrades
• - Security Lighting
• - Switchboard upgrades
• - Test and Tag
• - Commercial Property
• - General Electrical Maintenance

```html
<!DOCTYPE html>
<html lang="en">
<head>
<meta charset="utf-8">
<title>Torvin Electrics Flyer</title>
<link rel="stylesheet" href="https://fonts.googleapis.com/css2?family=Saira+Condensed:wght@700&family=Saira:wght@500;600&family=Montserrat:wght@400;500;600&display=swap">
<style>
  :root {
    --blue-bright: #0292cd;
    --blue-mid: #33a6d7;
    --blue-light: #85cae6;
    --blue-deep: #3176b5;
    --charcoal: #333333;
    --ink: #1b1b1b;
    --white: #ffffff;
    --grey: #5c5c5c;
    --grey-dark: #474747;
    --page-bg: #f3f3f3;
  }
  * { box-sizing: border-box; margin: 0; padding: 0; }
  html, body { width: 700px; height: 1200px; overflow: hidden; background: var(--page-bg); }
  .canvas { position: relative; width: 700px; height: 1200px; }
  .flyer {
    position: absolute; left: 30px; top: 145px;
    width: 478px; height: 679px;
    transform: scale(1.339); transform-origin: 0 0;
    background: var(--white);
    box-shadow: 0 2px 6px rgba(0,0,0,.18);
    font-family: "Montserrat", Arial, sans-serif;
    color: var(--charcoal);
    overflow: hidden;
  }
  .offer-box {
    position: absolute; left: 22px; top: 20px; width: 241px; height: 81px;
    background: var(--grey-dark); padding: 6px 0 0 16px;
  }
  .offer-title {
    font-family: "Saira Condensed", "Arial Narrow", sans-serif; font-weight: 700;
    font-size: 46px; line-height: 44px; color: var(--white);
    transform: skewX(-10deg); transform-origin: left bottom; letter-spacing: -0.5px;
  }
  .offer-sub {
    font-family: "Saira", Arial, sans-serif; font-weight: 600;
    font-size: 20px; line-height: 24px; color: var(--blue-light); letter-spacing: 0.3px;
  }
  .brand {
    position: absolute; left: 284px; top: 30px; display: flex; align-items: center; gap: 8px;
  }
  .brand-mark { width: 38px; height: 38px; border-radius: 50%; background: var(--blue-bright); flex: none; }
  .brand-name { font-weight: 600; font-size: 15.5px; line-height: 18px; color: var(--grey-dark); white-space: nowrap; }
  .photo { position: absolute; }
  .photo-kitchen { left: 22px; top: 106px; width: 435px; height: 189px; background: linear-gradient(180deg, #e9e9e7 0%, #d7d4cf 55%, #b9b5ae 100%); }
  .photo-living { left: 272px; top: 300px; width: 185px; height: 101px; background: linear-gradient(180deg, #ecedee 0%, #d9dad8 100%); }
  .photo-hall { left: 272px; top: 407px; width: 185px; height: 105px; background: linear-gradient(180deg, #dedfe0 0%, #b8bcbd 100%); }
  .photo-bath { left: 272px; top: 517px; width: 185px; height: 106px; background: linear-gradient(180deg, #e6e8e8 0%, #c9cccb 100%); }
  .led-box {
    position: absolute; left: 22px; top: 300px; width: 244px; height: 59px;
    background: var(--grey-dark); padding: 3px 0 0 9px;
  }
  .led-title { font-family: "Saira", Arial, sans-serif; font-weight: 500; font-size: 28px; line-height: 32px; color: var(--blue-light); }
  .led-sub { font-size: 16.5px; line-height: 20px; font-weight: 500; color: var(--white); white-space: nowrap; }
  .services { position: absolute; left: 27px; top: 366px; width: 240px; }
  .services-heading { font-size: 14px; line-height: 18px; font-weight: 500; color: var(--ink); }
  .services-heading .accent { color: var(--blue-deep); display: block; }
  .service-list { list-style: none; margin-top: 3px; }
  .service-list li { font-size: 10.5px; line-height: 14.6px; color: var(--charcoal); display: flex; align-items: center; padding-left: 4px; white-space: nowrap; }
  .service-list svg { width: 7px; height: 7px; margin-right: 12px; flex: none; }
  .terms-note { position: absolute; left: 27px; top: 628px; font-size: 8px; line-height: 10px; color: var(--grey); }
  .credentials { position: absolute; left: 272px; top: 627px; display: flex; gap: 3px; }
  .credential { font-size: 9px; line-height: 15px; color: var(--white); padding: 0 5px; font-weight: 500; white-space: nowrap; }
  .credential-licence { background: var(--blue-deep); width: 76px; }
  .credential-abn { background: var(--grey-dark); width: 106px; }
  .contact-bar {
    position: absolute; left: 0; bottom: 0; width: 478px; height: 32px;
    background: var(--grey-dark); display: flex; align-items: center; justify-content: center; gap: 14px;
    color: var(--white); font-size: 10.5px; white-space: nowrap;
  }
  .contact { display: flex; align-items: center; gap: 6px; }
  .contact-phone { font-weight: 600; }
  .contact svg { flex: none; }
  .social-square { width: 8px; height: 8px; background: var(--blue-mid); }
</style>
</head>
<body>
<div class="canvas">
  <div class="flyer">
    <div class="offer-box">
      <div class="offer-title">10% OFF ANY</div>
      <div class="offer-sub">ELECTRICAL WORK</div>
    </div>
    <div class="brand">
      <div class="brand-mark"></div>
      <div class="brand-name">Torvin Electrics</div>
    </div>

    <div class="photo photo-kitchen" role="img" aria-label="Modern kitchen with pendant lights and island bench"></div>

    <div class="led-box">
      <div class="led-title">FREE LED</div>
      <div class="led-sub">downlights on installation</div>
    </div>

    <div class="photo photo-living" role="img" aria-label="Bright living room with downlights"></div>
    <div class="photo photo-hall" role="img" aria-label="Dining area with pendant light"></div>
    <div class="photo photo-bath" role="img" aria-label="Bathroom with feature lighting"></div>

    <div class="services">
      <h2 class="services-heading">All residential and commercial<span class="accent">Electrical services</span></h2>
      <ul class="service-list">
        <li><svg viewBox="0 0 8 8"><circle cx="4" cy="4" r="4" fill="#3176b5"/><path d="M2.2 4.1l1.2 1.1 2.4-2.4" stroke="#fff" stroke-width="1" fill="none"/></svg>New Home installations</li>
        <li><svg viewBox="0 0 8 8"><circle cx="4" cy="4" r="4" fill="#3176b5"/><path d="M2.2 4.1l1.2 1.1 2.4-2.4" stroke="#fff" stroke-width="1" fill="none"/></svg>Commercial projects</li>
        <li><svg viewBox="0 0 8 8"><circle cx="4" cy="4" r="4" fill="#3176b5"/><path d="M2.2 4.1l1.2 1.1 2.4-2.4" stroke="#fff" stroke-width="1" fill="none"/></svg>Shop fit outs</li>
        <li><svg viewBox="0 0 8 8"><circle cx="4" cy="4" r="4" fill="#3176b5"/><path d="M2.2 4.1l1.2 1.1 2.4-2.4" stroke="#fff" stroke-width="1" fill="none"/></svg>Renovations</li>
        <li><svg viewBox="0 0 8 8"><circle cx="4" cy="4" r="4" fill="#3176b5"/><path d="M2.2 4.1l1.2 1.1 2.4-2.4" stroke="#fff" stroke-width="1" fill="none"/></svg>Smoke Detectors</li>
        <li><svg viewBox="0 0 8 8"><circle cx="4" cy="4" r="4" fill="#3176b5"/><path d="M2.2 4.1l1.2 1.1 2.4-2.4" stroke="#fff" stroke-width="1" fill="none"/></svg>Air Conditioning and Ceiling Fans</li>
        <li><svg viewBox="0 0 8 8"><circle cx="4" cy="4" r="4" fill="#3176b5"/><path d="M2.2 4.1l1.2 1.1 2.4-2.4" stroke="#fff" stroke-width="1" fill="none"/></svg>Garden Lighting</li>
        <li><svg viewBox="0 0 8 8"><circle cx="4" cy="4" r="4" fill="#3176b5"/><path d="M2.2 4.1l1.2 1.1 2.4-2.4" stroke="#fff" stroke-width="1" fill="none"/></svg>Oven and Cooktop Installations</li>
        <li><svg viewBox="0 0 8 8"><circle cx="4" cy="4" r="4" fill="#3176b5"/><path d="M2.2 4.1l1.2 1.1 2.4-2.4" stroke="#fff" stroke-width="1" fill="none"/></svg>Power Point installation</li>
        <li><svg viewBox="0 0 8 8"><circle cx="4" cy="4" r="4" fill="#3176b5"/><path d="M2.2 4.1l1.2 1.1 2.4-2.4" stroke="#fff" stroke-width="1" fill="none"/></svg>LED lighting upgrades</li>
        <li><svg viewBox="0 0 8 8"><circle cx="4" cy="4" r="4" fill="#3176b5"/><path d="M2.2 4.1l1.2 1.1 2.4-2.4" stroke="#fff" stroke-width="1" fill="none"/></svg>Security Lighting</li>
        <li><svg viewBox="0 0 8 8"><circle cx="4" cy="4" r="4" fill="#3176b5"/><path d="M2.2 4.1l1.2 1.1 2.4-2.4" stroke="#fff" stroke-width="1" fill="none"/></svg>Switchboard upgrades</li>
        <li><svg viewBox="0 0 8 8"><circle cx="4" cy="4" r="4" fill="#3176b5"/><path d="M2.2 4.1l1.2 1.1 2.4-2.4" stroke="#fff" stroke-width="1" fill="none"/></svg>Test and Tag</li>
        <li><svg viewBox="0 0 8 8"><circle cx="4" cy="4" r="4" fill="#3176b5"/><path d="M2.2 4.1l1.2 1.1 2.4-2.4" stroke="#fff" stroke-width="1" fill="none"/></svg>Commercial Property</li>
        <li><svg viewBox="0 0 8 8"><circle cx="4" cy="4" r="4" fill="#3176b5"/><path d="M2.2 4.1l1.2 1.1 2.4-2.4" stroke="#fff" stroke-width="1" fill="none"/></svg>General Electrical Maintenance</li>
      </ul>
    </div>
    <p class="terms-note">*Terms and conditions apply</p>

    <div class="credentials">
      <div class="credential credential-licence">Lic no. 51827</div>
      <div class="credential credential-abn">ABN 48 309 172 665</div>
    </div>

    <div class="contact-bar">
      <div class="contact contact-phone">
        <svg width="11" height="11" viewBox="0 0 24 24"><path d="M6.6 10.8a15 15 0 0 0 6.6 6.6l2.2-2.2a1 1 0 0 1 1-.25 11.4 11.4 0 0 0 3.6.57 1 1 0 0 1 1 1V20a1 1 0 0 1-1 1A17 17 0 0 1 3 4a1 1 0 0 1 1-1h3.5a1 1 0 0 1 1 1c0 1.25.2 2.45.57 3.57a1 1 0 0 1-.25 1z" fill="none" stroke="#85cae6" stroke-width="2"/></svg>
        <span>0457 613 948</span>
      </div>
      <div class="contact">
        <svg width="10" height="8" viewBox="0 0 10 8"><rect x="0.5" y="0.5" width="9" height="7" fill="none" stroke="#85cae6"/><path d="M0.5 0.5l4.5 4 4.5-4" fill="none" stroke="#85cae6"/></svg>
        <span>admin@torvinelectrics.com.au</span>
      </div>
      <div class="contact">
        <span class="social-square"></span>
        <span>/TorvinElectrics</span>
      </div>
    </div>
  </div>
</div>
</body>
</html>
```